Need a logo and business card design for my electrical company.
Company name is Kestrel Grid Electrical
In the bottow right hand corner i need
E.C. 784213 for the momument till i get my contractors license number sent to me.
Design i want black back ground with a picture of Thor's hammer and lighting hitting the top of it.

Electrical

Owner Darren Holcott Phone number 0471382905 email kestrelgridelectrical@nerimail.com facebook page Kestrel Grid Electrical

```html
<!DOCTYPE html>
<html lang="en">
<head>
<meta charset="UTF-8">
<title>Kestrel Grid Electrical – Business Card</title>
<link href="https://fonts.googleapis.com/css2?family=Arimo:wght@400;700&display=swap" rel="stylesheet">
<style>
  :root {
    --page-bg: #ececec;
    --panel-black: #000000;
    --card-light-center: #d3f6ff;
    --card-light-edge: #c9cffb;
    --ink: #2b2b2b;
    --brand-blue: #1e8fff;
    --bolt-deep: #1b3fd6;
    --bolt-bright: #22c8f0;
  }
  * { margin: 0; padding: 0; box-sizing: border-box; }
  html, body {
    width: 1200px;
    height: 851px;
    overflow: hidden;
    background: var(--page-bg);
    font-family: "Arimo", Arial, sans-serif;
  }
  .card {
    position: absolute;
    left: 50px;
    top: 87px;
    width: 1100px;
    height: 677px;
    overflow: hidden;
    background: radial-gradient(ellipse 62% 70% at 66% 55%, var(--card-light-center) 0%, var(--card-light-edge) 100%);
    box-shadow: 0 6px 18px rgba(0,0,0,0.25);
  }
  .brand-panel {
    position: absolute;
    left: 0; top: 0;
    width: 263px;
    height: 100%;
    background: var(--panel-black);
  }
  .lightning-art {
    position: absolute;
    left: 0; top: 0;
    width: 220px;
    height: 100%;
    background:
      radial-gradient(ellipse 40% 30% at 40% 20%, rgba(27,63,214,0.45), transparent 70%),
      radial-gradient(ellipse 45% 35% at 50% 80%, rgba(34,200,240,0.40), transparent 70%),
      linear-gradient(180deg, rgba(27,63,214,0.15), rgba(34,200,240,0.15));
  }
  .brand-disc {
    position: absolute;
    left: 81px;
    top: 93px;
    width: 356px;
    height: 356px;
    border-radius: 50%;
    background: var(--panel-black);
    display: flex;
    align-items: center;
    justify-content: center;
  }
  .brand-name {
    color: var(--brand-blue);
    font-weight: 700;
    font-size: 40px;
    line-height: 1.15;
    text-align: center;
    text-transform: uppercase;
    letter-spacing: 1px;
  }
  .owner-name {
    position: absolute;
    left: 538px;
    top: 128px;
    font-size: 36px;
    font-weight: 700;
    color: var(--ink);
  }
  .contact-list {
    position: absolute;
    left: 518px;
    top: 212px;
    list-style: none;
  }
  .contact-item {
    display: flex;
    align-items: center;
    height: 68px;
    font-size: 31px;
    color: var(--ink);
  }
  .contact-icon {
    width: 46px;
    height: 46px;
    margin-right: 24px;
    flex: none;
  }
  .licence-number {
    position: absolute;
    right: 84px;
    top: 574px;
    font-size: 33px;
    color: var(--ink);
  }
</style>
</head>
<body>
  <div class="card">
    <div class="brand-panel">
      <div class="lightning-art" role="img" aria-label="Blue lightning bolts striking down the black panel"></div>
    </div>
    <div class="brand-disc">
      <p class="brand-name">Kestrel Grid<br>Electrical</p>
    </div>

    <h1 class="owner-name">Darren Holcott</h1>

    <ul class="contact-list">
      <li class="contact-item">
        <svg class="contact-icon" viewBox="0 0 46 46" aria-hidden="true">
          <circle cx="23" cy="23" r="20" fill="none" stroke="#2b2b2b" stroke-width="2.5"/>
          <path d="M17 13 q-4 2 -3 7 q3 10 13 14 q5 1 7 -3 l-4 -4 q-2 2 -4 1 q-5 -3 -7 -8 q-1 -2 1 -4 z" fill="#2b2b2b"/>
        </svg>
        Phone number
      </li>
      <li class="contact-item">
        <svg class="contact-icon" viewBox="0 0 46 46" aria-hidden="true">
          <rect x="3" y="12" width="40" height="24" fill="#2b2b2b"/>
          <path d="M3 12 L23 27 L43 12" fill="none" stroke="#e9f6ff" stroke-width="2"/>
        </svg>
        Email address
      </li>
      <li class="contact-item">
        <svg class="contact-icon" viewBox="0 0 46 46" aria-hidden="true">
          <g fill="none" stroke="#2b2b2b" stroke-width="2.5">
            <circle cx="23" cy="23" r="20"/>
            <ellipse cx="23" cy="23" rx="9" ry="20"/>
            <line x1="23" y1="3" x2="23" y2="43"/>
            <line x1="3" y1="23" x2="43" y2="23"/>
            <path d="M6 13 H40 M6 33 H40"/>
          </g>
        </svg>
        www.company.com
      </li>
      <li class="contact-item">
        <svg class="contact-icon" viewBox="0 0 46 46" aria-hidden="true">
          <path d="M23 4 L43 18 H3 Z" fill="#2b2b2b"/>
          <rect x="5" y="21" width="36" height="20" fill="#2b2b2b"/>
          <rect x="10" y="27" width="11" height="11" fill="#e9f6ff"/>
          <rect x="25" y="27" width="11" height="11" fill="#e9f6ff"/>
        </svg>
        Address
      </li>
    </ul>

    <p class="licence-number">E.C. 784213</p>
  </div>
</body>
</html>
```